2018 Harborline Constable's Legal Companion

Cover, spine and back cover for Police Officer Law book. The overall size of the cover is 18.82 x 11 (with the .25 inch bleed it is 19.32 x 11.5) and the spine is 1.82 x 11 plus (1.82 x 11.5 with the bleed). The book also has a companion cruiser good for motor vehicle law which is smaller about 5X7 inches with a spiral binding. The Motor Vehicle guide should have a similar design but with a motor vehicle theme to it. The year (2018) should be prominent because it changes every year. I attached the last two book designs. I'd like them to be distinctively different each year.

Target Market(s)

Massachusetts Police Officers

Requirements
Must have
• Companion motor vehicle guide with similar design yet a motor vehicle theme or twist to it. Professional text book type look.
Nice to have
• real life image or images
Should not have
• Images of police who are obviously not US police.

```html
<!DOCTYPE html>
<html lang="en">
<head>
<meta charset="utf-8">
<title>2018 Harborline Constable's Motor Vehicle Guide – Cover Spread</title>
<link rel="stylesheet" href="https://fonts.googleapis.com/css2?family=Arimo:wght@700&family=Montserrat:wght@700&family=Tinos:wght@400;700&display=swap">
<style>
  :root {
    --page: #ffffff;
    --navy-deep: #0b1240;
    --navy-mid: #16267a;
    --navy-glow: #1f3398;
    --gold: #fdc42a;
    --yellow: #ffdd00;
    --ink-navy: #0f1d66;
    --white: #ffffff;
    --siren-red: #c0141c;
    --siren-blue: #3b3fb8;
  }
  html, body {
    margin: 0;
    padding: 0;
    width: 1200px;
    height: 747px;
    overflow: hidden;
    background: var(--page);
  }
  .cover-spread {
    display: block;
    width: 1200px;
    height: 747px;
  }
  .serif-bold { font-family: "Tinos", "Times New Roman", serif; font-weight: 700; }
  .serif { font-family: "Tinos", "Times New Roman", serif; font-weight: 400; }
  .year { font-family: "Arimo", Arial, sans-serif; font-weight: 700; }
  .author { font-family: "Montserrat", Arial, sans-serif; font-weight: 700; }
  .imprint { font-family: "Arimo", Arial, sans-serif; font-weight: 700; }
</style>
</head>
<body>
<svg class="cover-spread" viewBox="0 0 1200 747" xmlns="http://www.w3.org/2000/svg">
  <defs>
    <radialGradient id="back-glow" cx="0.55" cy="0.55" r="0.75">
      <stop offset="0" stop-color="var(--navy-glow)"/>
      <stop offset="0.6" stop-color="var(--navy-mid)"/>
      <stop offset="1" stop-color="var(--navy-deep)"/>
    </radialGradient>
    <radialGradient id="front-glow" cx="0.5" cy="0.7" r="0.8">
      <stop offset="0" stop-color="var(--navy-glow)"/>
      <stop offset="0.6" stop-color="var(--navy-mid)"/>
      <stop offset="1" stop-color="var(--navy-deep)"/>
    </radialGradient>
    <linearGradient id="cruiser-tone" x1="0" y1="0" x2="1" y2="0.6">
      <stop offset="0" stop-color="var(--siren-red)"/>
      <stop offset="0.45" stop-color="#7a2a6a"/>
      <stop offset="1" stop-color="var(--siren-blue)"/>
    </linearGradient>
    <linearGradient id="cruiser-fade" x1="0" y1="0" x2="0" y2="1">
      <stop offset="0" stop-color="#000" stop-opacity="0"/>
      <stop offset="0.55" stop-color="#000" stop-opacity="0"/>
      <stop offset="1" stop-color="var(--navy-mid)" stop-opacity="1"/>
    </linearGradient>
  </defs>

  <!-- back cover -->
  <rect class="back-panel" x="26" y="58" width="522" height="638" fill="url(#back-glow)"/>
  <!-- spine -->
  <rect class="spine-panel" x="548" y="58" width="100" height="638" fill="var(--navy-deep)"/>
  <!-- front cover -->
  <rect class="front-panel" x="648" y="58" width="522" height="638" fill="url(#front-glow)"/>

  <!-- cruiser photo area -->
  <g class="hero-photo" role="img" aria-label="Photo of a police cruiser at night with red and blue roof lights flashing">
    <rect x="648" y="58" width="522" height="392" fill="url(#cruiser-tone)" opacity="0.85"/>
    <rect x="648" y="58" width="522" height="392" fill="url(#cruiser-fade)"/>
  </g>

  <!-- fold lines -->
  <line x1="548" y1="58" x2="548" y2="696" stroke="#2a3a8c" stroke-width="0.8"/>
  <line x1="648" y1="58" x2="648" y2="696" stroke="#2a3a8c" stroke-width="0.8"/>

  <!-- gold waves -->
  <path class="wave-back" d="M26 640 C120 626 230 626 340 640 C430 652 500 662 648 668 L648 696 L26 696 Z" fill="var(--gold)"/>
  <path class="wave-front" d="M648 668 C760 672 860 660 960 646 C1040 636 1110 632 1170 636 L1170 696 L648 696 Z" fill="var(--gold)"/>

  <!-- back cover imprint -->
  <text class="imprint" x="104" y="676" font-size="13" fill="var(--ink-navy)">2018 Whitcombe Consulting LLC. All Rights Reserved</text>

  <!-- spine titles -->
  <text class="year" transform="translate(632,632) rotate(-90)" font-size="95" fill="var(--white)" textLength="188" lengthAdjust="spacingAndGlyphs">2018</text>
  <text class="serif-bold" transform="translate(596,420) rotate(-90)" font-size="23" fill="var(--yellow)" textLength="250" lengthAdjust="spacingAndGlyphs">Harborline Constable's</text>
  <text class="serif" transform="translate(624,420) rotate(-90)" font-size="27" fill="var(--yellow)" textLength="340" lengthAdjust="spacingAndGlyphs">MOTOR VEHICLE GUIDE</text>

  <!-- spine publisher mark -->
  <g class="publisher-mark">
    <circle cx="598" cy="656" r="11" fill="var(--ink-navy)"/>
    <text class="imprint" x="598" y="683" font-size="9" fill="var(--ink-navy)" text-anchor="middle">Whitcombe</text>
  </g>

  <!-- front cover titles -->
  <text class="serif-bold" x="904" y="264" font-size="25" fill="var(--white)" text-anchor="middle">Harborline Constable's</text>
  <text class="year" x="909" y="416" font-size="196" fill="var(--yellow)" text-anchor="middle" textLength="414" lengthAdjust="spacingAndGlyphs">2018</text>
  <text class="serif" x="1104" y="450" font-size="29" fill="var(--white)" text-anchor="end">Motor Vehicle Guide</text>

  <!-- author -->
  <text class="author" x="919" y="586" font-size="22" fill="var(--gold)" text-anchor="middle">Lieutenant Daniel R. Whitcombe, Esq.</text>
  <text class="serif" x="920" y="608" font-size="16" fill="var(--white)" text-anchor="middle">The Law Officer</text>
</svg>
</body>
</html>
```